Creative, Modern and Conversion based Web Design

Kolvex Digital has recently launched a new logo and as part of our companies rebranding, we need a new website aimed towards the UK B2B marketplace.

The website needs to deliver a modern and creative website design whilst ensuring the design is tailored towards conversion optimisation.

This site must drive point of contact either from an online form, via a direct telephone call or Skype connection.

Our sales are all offline so the website will be a simple, elegant and stunning information portal.

Kolvex Digital offers Digital Marketing services to companies throughout the UK - our target audiences are companies that turnover a minimum of 3 million pounds a year and as such we need to deliver a professional image that installs confidence in our companies abilities.

We do not like websites that are reliant upon stock photography - we are happy for stock photography to be used in a small way however the site must not look like a template filled with stock photography.

What do we do

We supply digital marketing services to those companies who demand a strong return on investment - our company prides itself on delivering successful campaigns that help establish long-term profitable relationships.

A lot of the information presented on our old site is relevant today however the design sucks. So please use the information on our current website as a foundation for your design content.

I am looking for several page designs including

"Home Page" Desktop Version
"Service Page" Desktop Version
"Blog Page" Desktop Version

"Home Page" Mobile Version
"Service Page" Mobile Version
"Blog Page" Mobile Version

In the 1st instance please only submit a single design for the "Home Page" Desktop Version - those designers that we are impressed with will be asked to complete the other designs before a winner is selected.

I like modern clean fonts - the site needs to welcome the reader and encourage them to absorb the information - not to overload and make them leave.

The site must be designed to naturally fit our companies new logo.

NO TEMPLATES

Target Market(s)

B2b - 3 million turnover and above

Industry/Entity Type

Digital Marketing

Number of Pages Required

3 page

Requirements
Must have
• Blended well with the companies logo
• We need conversion optimisation to be a huge part of the design - we considered a conversation when a potential customer reaches out to use via - web form, telephone or skype
• The current content on the old website fits today's business but the design sucks.
• www.kolvexdigital-example.com
Nice to have
• We need 3 pages (in 2 variants Desktop and Mobile)
• Home Page
• Service Page
• Blog Page
• Please only deliver the "Home Page" desktop version - if we are happy with your design we will aks for the additional pages
Should not have
• No templates and not stock photo heavy design

```html
<!DOCTYPE html>
<html lang="en">
<head>
<meta charset="utf-8">
<title>Kolvex Digital – Search marketing that actually delivers</title>
<link href="https://fonts.googleapis.com/css2?family=Poppins:wght@300;400;500;600;700&display=swap" rel="stylesheet">
<style>
:root{
  --purple:#5a4ee6;
  --purple-light:#7b6ff5;
  --navy:#0c4a8e;
  --blue:#1f62ad;
  --blue-band:#2d6cae;
  --ink:#1d1d2b;
  --grey:#5d6170;
  --line:#e3e6ee;
  --tile:#eef1fb;
  --lavender:#f1f2fb;
  --white:#ffffff;
  --footer:#1b3f7a;
}
*{box-sizing:border-box;margin:0;padding:0}
html,body{width:1200px;height:4813px;overflow:hidden}
body{font-family:'Poppins',sans-serif;color:var(--ink);background:var(--white);position:relative}
section,header,footer{position:absolute;left:0;width:1200px}
.btn{display:inline-block;border:2px solid var(--navy);border-radius:30px;font-size:13px;font-weight:600;letter-spacing:.5px;color:var(--navy);text-transform:uppercase;padding:9px 24px;text-decoration:none}
.btn-solid{background:var(--white);border-color:var(--white);color:var(--navy)}
.art{position:absolute;border-radius:16px}

/* header */
.site-header{top:0;height:112px;display:flex;align-items:center;justify-content:space-between;padding:0 90px}
.brand{display:flex;align-items:center;gap:12px;font-size:24px;font-weight:600;color:var(--ink)}
.brand-mark{width:26px;height:26px;background:var(--navy)}
.nav{display:flex;gap:44px;list-style:none}
.nav a{font-size:13px;font-weight:600;text-transform:uppercase;color:var(--ink);text-decoration:none}

/* hero */
.hero{top:112px;height:790px;background:linear-gradient(180deg,#4c44dc 0%,#6a5ff2 100%);text-align:center;color:var(--white)}
.hero h1{margin-top:205px;font-size:42px;font-weight:400}
.hero p{font-size:23px;font-weight:300;line-height:1.3;margin:8px auto 0;width:600px}
.hero-art{left:200px;top:360px;width:820px;height:400px;border-radius:200px 200px 40px 40px;background:radial-gradient(ellipse at 55% 45%,#ffffff 0%,#e8ebfb 55%,#b9b6f5 100%)}

/* partners */
.partners{top:902px;height:120px;display:flex;align-items:center;justify-content:center;gap:60px;border-bottom:1px solid var(--line)}
.badge{width:120px;height:40px;border-radius:6px;background:#c9ccd6}

/* roi */
.roi{top:1060px;height:260px;text-align:center}
.roi h2{font-size:28px;font-weight:700;color:var(--navy);line-height:1.3}
.roi p{width:880px;margin:20px auto 0;font-size:15px;line-height:1.75;color:var(--grey)}
.roi p span{color:var(--blue)}

/* in-house */
.inhouse{top:1345px;height:240px;border-top:1px solid var(--line);border-bottom:1px solid var(--line)}
.inhouse-copy{position:absolute;left:130px;top:55px}
.inhouse h3{font-size:21px;font-weight:500}
.inhouse p{font-size:17px;color:var(--grey);margin:6px 0 20px}
.inhouse p strong{color:var(--ink)}
.partner-panel{position:absolute;left:830px;top:0;width:370px;height:240px;border-left:1px solid var(--line);display:flex;align-items:center;justify-content:center}
.partner-badge{width:230px;height:150px;border-radius:10px;background:#e4e7f0}

/* services */
.services{top:1605px;height:780px}
.tile{position:absolute;width:322px;height:242px;background:var(--tile);text-align:center;padding-top:30px}
.tile h4{font-size:15px;font-weight:500}
.tile .icon{position:relative;display:block;margin:24px auto 0;width:150px;height:120px;border-radius:14px;background:linear-gradient(135deg,#bcd2f5,#f4b3a0)}
.tile-feature{background:var(--navy);color:var(--white);padding-top:70px}
.tile-feature h4{font-size:24px;font-weight:600}
.tile-feature p{font-size:14px;margin:6px 0 20px}
.tile-feature .btn{border-color:var(--white);color:var(--white);font-size:11px;padding:7px 18px}

/* stats */
.stats{top:2423px;height:340px;background:var(--lavender);text-align:center}
.stats h3{display:inline-block;margin-top:55px;font-size:21px;font-weight:500;padding-bottom:8px;border-bottom:2px solid var(--ink)}
.stat-row{display:flex;justify-content:center;gap:90px;margin-top:40px}
.stat{width:170px}
.stat svg{display:block;margin:0 auto}
.stat b{display:block;font-size:50px;font-weight:700;color:var(--blue);line-height:1.2}
.stat span{font-size:15px;color:var(--grey)}

/* diy */
.diy{top:2801px;height:410px}
.diy-photos{left:0;top:0;width:584px;height:410px;border-radius:0;background:linear-gradient(135deg,#cfd6e2,#f1eee8 60%,#b8c3d4)}
.diy-copy{position:absolute;left:645px;top:85px;width:470px}
.diy h3{font-size:21px;font-weight:600}
.diy .tag{display:inline-block;background:var(--navy);color:var(--white);font-size:13px;font-weight:600;padding:4px 14px;margin:8px 0 18px}
.diy p{font-size:14px;line-height:1.75;color:var(--grey)}

/* process */
.process{top:3273px;height:500px;text-align:center}
.process .tag{display:inline-block;background:var(--navy);color:var(--white);font-size:13px;font-weight:600;padding:4px 14px}
.process h2{font-size:24px;font-weight:600;margin-top:8px}
.steps{position:absolute;left:70px;top:130px;width:1060px;height:360px}
.step{position:absolute;top:0;width:245px;text-align:center}
.step .dot{width:200px;height:200px;border-radius:50%;margin:0 auto;background:var(--white);box-shadow:0 8px 30px rgba(20,40,90,.12);display:flex;flex-direction:column;justify-content:center}
.step b{font-size:40px;font-weight:700}
.step small{font-size:12px;font-weight:700;letter-spacing:.5px}
.step p{font-size:13px;line-height:1.7;color:var(--grey);margin-top:30px}

.pricing{top:3773px;height:80px;display:flex;align-items:center;justify-content:center;gap:22px}
.pricing span{font-size:21px;font-weight:500}

/* contact band */
.talk{top:3851px;height:385px;background:linear-gradient(180deg,#1f5c9f,#3c7dbd);text-align:center;color:var(--white)}
.talk h2{margin-top:70px;font-size:36px;font-weight:600}
.talk p{font-size:16px;font-weight:300;margin:4px 0 28px}
.talk svg{position:absolute;left:0;bottom:0}

/* locations */
.locations{top:4236px;height:410px;text-align:center}
.map{left:230px;top:10px;width:740px;height:380px;background:radial-gradient(ellipse at center,#e7e9ee 0%,#f5f6f8 70%,#ffffff 100%)}
.locations h2{position:relative;margin-top:140px;font-size:24px;font-weight:600}
.cities{position:relative;width:880px;margin:18px auto 0;font-size:13px;line-height:1.9;word-spacing:8px}
.locations .btn{position:relative;margin-top:24px}

/* footer */
.contact-strip{top:4640px;height:125px;display:flex;justify-content:center;gap:150px;align-items:center}
.contact-item{display:flex;align-items:center;gap:16px}
.contact-item b{display:block;font-size:12px;font-weight:700;text-transform:uppercase}
.contact-item span{font-size:13px;color:var(--grey)}
.site-footer{top:4765px;height:48px;background:var(--footer);color:var(--white);font-size:12px;display:flex;align-items:center;justify-content:center}
</style>
</head>
<body>

<header class="site-header">
  <div class="brand"><span class="brand-mark"></span>Kolvex Digital</div>
  <ul class="nav">
    <li><a href="#">Home</a></li>
    <li><a href="#">About Us</a></li>
    <li><a href="#">Services</a></li>
    <li><a href="#">White Label Link Building</a></li>
    <li><a href="#">Blog</a></li>
    <li><a href="#">Contact Us</a></li>
  </ul>
</header>

<section class="hero">
  <h1>Search marketing that actually delivers</h1>
  <p>Search marketing is our forte. Our client results highlight just how good we do it.</p>
  <div class="art hero-art" role="img" aria-label="Illustration of people working around a large phone with charts and an SEO sign"></div>
</section>

<section class="partners" aria-label="Accreditations">
  <div class="badge"></div><div class="badge"></div><div class="badge"></div>
  <div class="badge"></div><div class="badge"></div><div class="badge"></div>
</section>

<section class="roi">
  <h2>Do you want to see an enviable ROI on search marketing?<br>It's possible – you've found us.</h2>
  <p>We know and understand the world of business. We know that ROI is the single most important metric in the marketing world. We've worked within some of the world's largest industries – such as finance, insurance, payday loans and health, where achieving above 100% ROI is often impossible. For us, it's just a challenge that can be overcome. Whether we're working with you to drive your <span>Pay-Per-Click Marketing, Organic Search Marketing (SEO), Email Marketing or Lead Filtering &amp; Delivery</span> – we always have your ROI in mind. That's why we're known as the ROI driven digital agency.</p>
</section>

<section class="inhouse">
  <div class="inhouse-copy">
    <h3>Handle your SEO in-house?</h3>
    <p>Consider using our industry-leading <strong>link outreach service</strong> to bolster your efforts.</p>
    <a class="btn" href="#">Contact us now</a>
  </div>
  <div class="partner-panel"><div class="partner-badge"></div></div>
</section>

<section class="services">
  <div class="tile" style="left:96px;top:0"><h4>Lead Filtering and Delivery</h4><span class="icon" role="img" aria-label="Illustration of reports and a magnifying glass"></span></div>
  <div class="tile" style="left:443px;top:0"><h4>Email Marketing</h4><span class="icon" role="img" aria-label="Illustration of an open envelope with icons"></span></div>
  <div class="tile" style="left:786px;top:0"><h4>Link Outreach</h4><span class="icon" role="img" aria-label="Illustration of a monitor with linked nodes"></span></div>
  <div class="tile" style="left:96px;top:270px"><span class="icon" style="margin-top:20px" role="img" aria-label="Illustration of a keyboard and charts"></span></div>
  <div class="tile tile-feature" style="left:443px;top:270px"><h4>OUR SERVICES</h4><p>We Offer a Full Range of Digital Marketing Services!</p><a class="btn" href="#">Get quote now</a></div>
  <div class="tile" style="left:786px;top:270px"><h4>Paid Search</h4><span class="icon" role="img" aria-label="Illustration of devices with payment symbols"></span></div>
  <div class="tile" style="left:96px;top:538px"><h4>Organic Search</h4><span class="icon" role="img" aria-label="Illustration of a search results screen"></span></div>
  <div class="tile" style="left:443px;top:538px"><h4>Social Media</h4><span class="icon" role="img" aria-label="Illustration of a laptop with social icons"></span></div>
  <div class="tile" style="left:786px;top:538px"><h4>UX &amp; CRO</h4><span class="icon" role="img" aria-label="Illustration of a growth chart on a screen"></span></div>
</section>

<section class="stats">
  <h3>We grow as our clients grow. That's what we love.</h3>
  <div class="stat-row">
    <div class="stat"><svg width="46" height="40" viewBox="0 0 46 40" fill="none" stroke="#9aa3c0" stroke-width="2"><circle cx="23" cy="13" r="8"/><path d="M8 38c2-10 28-10 30 0"/></svg><b>117</b><span>Satisfied Clients</span></div>
    <div class="stat"><svg width="46" height="40" viewBox="0 0 46 40" fill="none" stroke="#9aa3c0" stroke-width="2"><rect x="4" y="4" width="38" height="32" rx="3"/><path d="M10 28l9-9 7 6 11-12"/></svg><b>215</b><span>Campaigns Finished</span></div>
    <div class="stat"><svg width="46" height="40" viewBox="0 0 46 40" fill="none" stroke="#9aa3c0" stroke-width="2"><circle cx="23" cy="20" r="16"/><path d="M15 20l6 6 11-12"/></svg><b>98</b><span>Success Rate</span></div>
    <div class="stat"><svg width="46" height="40" viewBox="0 0 46 40" fill="none" stroke="#9aa3c0" stroke-width="2"><path d="M8 12h24v14a10 10 0 0 1-10 10h-4A10 10 0 0 1 8 26z"/><path d="M32 16h4a5 5 0 0 1 0 10h-4"/></svg><b>1,798</b><span>Cups of Coffee</span></div>
  </div>
</section>

<section class="diy">
  <div class="art diy-photos" role="img" aria-label="Collage of office photos: team meeting, laptop on a desk and a presentation"></div>
  <div class="diy-copy">
    <h3>Handle SEO Yourself? Perfect.</h3>
    <span class="tag">Hassle-Free Link Placements That Drive Rankings</span>
    <p>Our link placements are used by some of the world's largest companies in the most difficult industries – such as payday loans, insurance, finance, health and legal. We use our link placement service in conjunction with our Organic Search (SEO) offerings, although some of our clients handle their SEO in-house and prefer to use our link placements to bolster their rankings.</p>
  </div>
</section>

<section class="process">
  <span class="tag">Work Process</span>
  <h2>Here's how our unique, link acquisition process works:</h2>
  <div class="steps">
    <svg width="1060" height="200" style="position:absolute;left:0;top:0" fill="none" stroke="#b9bfcf" stroke-width="1.5" stroke-dasharray="5 6"><path d="M222 100 C260 20 300 20 340 100"/><path d="M495 100 C535 20 575 20 612 100"/><path d="M768 100 C808 20 848 20 885 100"/></svg>
    <div class="step" style="left:0"><div class="dot"><b>01</b><small>RESEARCH</small></div><p>We take your client's URLs and their business sector (or your own sites), and we utilise our connections to try and secure a link placement.</p></div>
    <div class="step" style="left:272px"><div class="dot"><b>02</b><small>DATA COLLECTION</small></div><p>All of the sites we outreach too are 100% genuine – we do not own nor control any of the sites.</p></div>
    <div class="step" style="left:545px"><div class="dot"><b>03</b><small>TARGETING</small></div><p>If a webmaster chooses to link to you it is of their own accord. They have decided to link to you. Thus you have earned a genuine link.</p></div>
    <div class="step" style="left:815px"><div class="dot"><b>04</b><small>RESULT</small></div><p>We will identify the most relevant page/post on their site, and work with the webmaster to weave your links into their existing content. We will write an additional sentence or two to make sure the anchor text fits in with the content.</p></div>
  </div>
</section>

<section class="pricing">
  <span>Want to learn more and get our pricing?</span>
  <a class="btn" href="#">Click here</a>
</section>

<section class="talk">
  <h2>Want To Improve Your ROI? Let's Talk</h2>
  <p>We'll never turn down an opportunity to discover how we can help grow your business.</p>
  <a class="btn btn-solid" href="#">Get started with us</a>
  <svg width="1200" height="110" viewBox="0 0 1200 110" preserveAspectRatio="none"><path d="M0 110 L0 70 C90 70 120 20 200 20 C280 20 300 80 380 80 C460 80 480 30 560 30 C640 30 660 90 740 90 C820 90 840 25 920 25 C1000 25 1030 75 1100 75 C1150 75 1180 60 1200 55 L1200 110 Z" fill="#ffffff"/></svg>
</section>

<section class="locations">
  <div class="art map" role="img" aria-label="Faint world map"></div>
  <h2>Locations We Cover (SEO)</h2>
  <p class="cities">Aberdeen Armagh Bangor Bath Belfast Birmingham Bradford Brighton Bristol Cambridge Canterbury Cardiff<br>Carlisle Chester Chichester Coventry Derby Derry Dundee Durham Edinburgh Ely Exeter Glasgow Gloucester</p>
  <a class="btn" href="#">See all locations</a>
</section>

<section class="contact-strip">
  <div class="contact-item"><svg width="40" height="40" viewBox="0 0 40 40" fill="none" stroke="#1d1d2b" stroke-width="1.8"><rect x="4" y="9" width="32" height="22" rx="2"/><path d="M4 11l16 12 16-12"/></svg><div><b>Mail us:</b><span>info@kolvexdigital-example.com</span></div></div>
  <div class="contact-item"><svg width="40" height="40" viewBox="0 0 40 40" fill="none" stroke="#1d1d2b" stroke-width="1.8"><path d="M10 5l6 1 2 8-4 3c2 4 5 7 9 9l3-4 8 2 1 6c-1 3-4 5-7 4C18 32 8 22 6 12c-1-3 1-6 4-7z"/></svg><div><b>Call us:</b><span>01632 960418</span></div></div>
  <div class="contact-item"><svg width="40" height="40" viewBox="0 0 40 40" fill="none" stroke="#1d1d2b" stroke-width="1.8"><circle cx="20" cy="20" r="15"/><path d="M20 11v9l6 4"/></svg><div><b>Working hours</b><span>9AM-5PM, MON-FRI</span></div></div>
</section>

<footer class="site-footer">© 2018 Kolvex Digital Limited. All rights reserved.</footer>

</body>
</html>
```